DORLIT HOMES Professional Home Buyers

Please see two files uploaded. One is my new LOGO (thanks Quenby) and the other gives the wording and pages desired. Of course I am open to suggestions to further enhance what I'm about. I don't want testimonials or houses to buy to appear but to have room for them when I'm ready. I am a real estate investor not a licensed real estate agent. For FAQ i want just the questions to appear and when they click on the question the answer appears and when they click on the question again the answer disappears. make sense? When you read my wording and my idea of pages you'll get an idea of what I'm about. Suggestions are welcomed.

Industry/Entity Type

Real Estate

Number of Pages Required

5+ page

Requirements
Must have
• FAQ pages only questions appear. They click on question the answer appears underneath. they click on question again, the answer disappears. Also, I of course, want my new LOGO to appear on each page I don't know if it will look better all by itself or blended in somehow? Call now 418-555-0193 on each page also. I will get a real phone number before website goes live. If you have a better way of wording what I'm describing please let me know, I am open to feedback
Nice to have
• Anything that the average homeowner can relate to (yea I know, that doesn't help you much, right?)
• Testimonial page and houses to buy page could be done with just the shell ready in the wings for when my business grows it will be ready all that it would need then are the wording and pictures to be uploaded onto the website page. make sense?
Should not have
• I don't want it too elegant or rich looking as I believe my audience will be mostly the average homeowner who needs help

```html
<!DOCTYPE html>
<html lang="en">
<head>
<meta charset="utf-8">
<title>DORLIT HOMES – Professional Home Buyers</title>
<link href="https://fonts.googleapis.com/css2?family=Montserrat:wght@400;600;700;800&family=Open+Sans:wght@400;600;700&display=swap" rel="stylesheet">
<style>
:root{
  --blue:#1976d2;
  --blue-light:#2b9be3;
  --navy:#0d3f86;
  --dark:#2b2b2b;
  --footer:#303030;
  --text:#555;
  --muted:#8a8a8a;
  --line:#dcdcdc;
  --white:#fff;
  --bg-soft:#f2f2f2;
}
*{box-sizing:border-box;margin:0;padding:0}
html,body{width:667px;height:1200px;overflow:hidden}
body{position:relative;font-family:"Open Sans",sans-serif;color:var(--text);background:var(--white)}
.abs{position:absolute}
h1,h2,h3,h4{font-family:"Montserrat",sans-serif}

/* header */
.site-header{left:0;top:0;width:667px;height:66px;background:var(--white);border-bottom:1px solid var(--line)}
.brand{left:18px;top:16px;display:flex;align-items:center;gap:7px}
.brand-mark{width:14px;height:14px;background:var(--blue)}
.brand-name{font-family:"Montserrat",sans-serif;font-weight:800;font-size:17px;color:var(--navy);letter-spacing:.5px}
.brand-sub{left:39px;top:37px;font-size:7px;color:var(--muted);letter-spacing:1px;font-weight:600}
.call{right:16px;top:6px;display:flex;align-items:center;gap:6px;font-size:9px;font-weight:700;color:var(--dark)}
.call-pill{background:var(--blue);color:var(--white);padding:3px 9px;border-radius:10px;display:flex;align-items:center;gap:4px}
.main-nav{left:198px;top:36px;display:flex;gap:20px;font-family:"Montserrat",sans-serif;font-size:9px;font-weight:700;color:var(--dark)}
.main-nav .active{color:var(--blue);border-bottom:2px solid var(--blue);padding-bottom:4px}

/* hero */
.hero{left:0;top:66px;width:667px;height:327px;background:linear-gradient(180deg,#9dc3e0 0%,#c9d7df 35%,#8f9a8a 62%,#4f6a3c 100%)}
.hero-arrow{top:140px}
.hero-text{left:0;top:248px;width:667px;text-align:center;color:var(--white)}
.hero-text .kicker{font-family:"Montserrat",sans-serif;font-weight:700;font-size:14px;letter-spacing:.5px}
.hero-text .headline{font-family:"Montserrat",sans-serif;font-weight:800;font-size:27px;margin-top:6px}

/* intro columns */
.intro{left:0;top:393px;width:667px;height:189px;background:var(--white);border-bottom:1px solid var(--line)}
.col{top:20px;width:195px}
.col h3{font-size:11px;font-weight:800;color:var(--dark)}
.col .sub{font-size:7.5px;color:var(--blue);margin:3px 0 8px;font-weight:600}
.col p{font-size:7px;line-height:1.5;color:var(--muted)}
.btn-mini{display:inline-block;margin-top:9px;background:var(--dark);color:var(--white);font-size:6.5px;font-weight:700;padding:4px 9px}
.quote-mark{font-family:Georgia,serif;font-size:34px;color:var(--line);line-height:.8;float:left;margin-right:4px}
.author{font-size:7px;color:var(--blue);text-align:right;margin-top:5px;font-style:italic}
.form-grid{display:grid;grid-template-columns:1fr 1fr;gap:5px}
.field{border:1px solid var(--line);height:17px;font-size:6.5px;color:var(--muted);padding:4px 5px}
.btn-submit{background:var(--blue);color:var(--white);font-size:7px;font-weight:700;padding:5px 12px;display:inline-block}

/* cash band */
.cash{left:0;top:582px;width:667px;height:229px;overflow:hidden}
.cash-title{left:18px;top:25px;color:var(--white);font-family:"Montserrat",sans-serif;font-weight:800;font-size:21px;line-height:1.05}
.cash-title span{font-weight:400}
.cash-copy{left:18px;top:110px;width:128px;font-size:7px;line-height:1.5;color:var(--white)}
.photo{border-radius:50%;border:5px solid var(--white)}
.benefits{left:448px;top:18px;list-style:none;color:var(--white);font-size:8px;font-weight:600;line-height:1.85}
.benefits li::before{content:"✓ ";color:#9fd4ff}
.fastest{left:440px;top:118px;color:var(--white);text-align:right;width:210px;line-height:1.1}
.fastest b{display:block;font-family:"Montserrat",sans-serif;font-weight:800;font-size:26px}
.fastest span{display:block;margin-top:4px;font-family:"Montserrat",sans-serif;font-size:14px;font-weight:600;white-space:nowrap}

/* more info bar */
.more-info{left:0;top:811px;width:667px;height:44px;background:var(--blue);color:var(--white);font-family:"Montserrat",sans-serif;font-size:15px;font-weight:600;text-align:center;line-height:44px;letter-spacing:.5px}

/* any condition */
.condition{left:0;top:855px;width:667px;height:189px;background:var(--bg-soft)}
.condition h2{left:250px;top:44px;font-size:17px;font-weight:800;color:var(--dark);white-space:nowrap}
.condition h2 em{font-style:normal;color:var(--blue)}
.condition p{left:250px;top:74px;width:390px;font-size:7.5px;line-height:1.55;color:var(--muted)}
.btn-quote{left:250px;top:126px;background:var(--blue);color:var(--white);font-size:8px;font-weight:700;padding:7px 14px}

/* footer */
.site-footer{left:0;top:1044px;width:667px;height:156px;background:var(--footer);color:#cfcfcf}
.fcol{top:16px}
.fcol h4{font-size:9px;font-weight:700;color:var(--white);margin-bottom:9px}
.fcol ul{list-style:none;font-size:7px;line-height:1.75}
.fcol ul li::before{content:"› ";color:var(--blue-light)}
.contact-row{display:flex;gap:6px;align-items:flex-start;font-size:7px;line-height:1.4;margin-bottom:8px}
.dot{width:11px;height:11px;border-radius:50%;background:var(--blue);flex:none}
.social-row{display:flex;align-items:center;gap:6px;font-size:7px;margin-bottom:7px}
.footer-brand{right:22px;top:60px;font-family:"Montserrat",sans-serif;font-weight:800;font-size:20px;color:#8c8c8c}
.copyright{right:22px;top:96px;font-size:6.5px;color:#9a9a9a;text-align:right;line-height:1.5}
</style>
</head>
<body>

<header class="site-header abs">
  <div class="brand abs"><span class="brand-mark"></span><span class="brand-name">DORLIT HOMES</span></div>
  <div class="brand-sub abs">PROFESSIONAL HOME BUYERS</div>
  <div class="call abs">Call Us:
    <span class="call-pill">
      <svg width="8" height="8" viewBox="0 0 24 24" fill="#fff"><path d="M6.6 10.8a15 15 0 006.6 6.6l2.2-2.2c.3-.3.7-.4 1-.2 1.1.4 2.3.6 3.6.6.6 0 1 .4 1 1V20c0 .6-.4 1-1 1C10.6 21 3 13.4 3 4c0-.6.4-1 1-1h3.5c.6 0 1 .4 1 1 0 1.3.2 2.5.6 3.6.1.3 0 .7-.2 1z"/></svg>
      418-555-0193
    </span>
  </div>
  <nav class="main-nav abs">
    <span class="active">HOME</span><span>ABOUT US</span><span>FAQ</span><span>CONTACT US</span><span>TESTIMONIALS</span><span>HOUSES TO BUY</span>
  </nav>
</header>

<section class="hero abs" role="img" aria-label="Photo of a two-storey suburban house with a sold sign on the front lawn">
  <svg class="hero-arrow abs" style="left:14px" width="16" height="30" viewBox="0 0 16 30"><path d="M14 2L2 15l12 13" stroke="#fff" stroke-width="3" fill="none"/></svg>
  <svg class="hero-arrow abs" style="right:14px" width="16" height="30" viewBox="0 0 16 30"><path d="M2 2l12 13L2 28" stroke="#fff" stroke-width="3" fill="none"/></svg>
  <div class="hero-text abs">
    <div class="kicker">DON'T WASTE ANOTHER PENNY ON EXPENSIVE REPAIRS!</div>
    <div class="headline">WE BUY HOUSES IN ANY CONDITION!</div>
  </div>
</section>

<section class="intro abs">
  <div class="col abs" style="left:18px">
    <h3>WELCOME TO DORLIT HOME</h3>
    <div class="sub">The Professional Home Buyers</div>
    <p>We are local investors who buy homes as they are. No agents, no fees and no repairs needed. We make a fair cash offer fast and you pick the closing date that fits your plans. Selling your house has never been this simple or this clear.</p>
    <span class="btn-mini">READ MORE</span>
  </div>
  <div class="col abs" style="left:236px">
    <h3>KNOW WHAT</h3>
    <div class="sub">Our Clients Has To Say</div>
    <p><span class="quote-mark">“</span>They gave me a fair offer within a day and closed when I was ready. No showings, no repairs and no stress at all. I would tell any homeowner in a tight spot to call them first before listing.</p>
    <div class="author">- Mr. Calder Wynn</div>
    <span class="btn-mini">READ MORE</span>
  </div>
  <div class="col abs" style="left:454px">
    <h3>DORLIT HOME</h3>
    <div class="sub">Get Your Free Quote</div>
    <div class="form-grid">
      <div class="field">First Name</div><div class="field">Last Name</div>
      <div class="field">Phone Number</div><div class="field">Email Id</div>
      <div class="field">Home Address</div><div class="field">Zip Code</div>
      <div class="field">Timeline</div><div class="field">Lowest Price</div>
    </div>
    <div style="margin-top:7px"><span class="btn-submit">SUBMIT</span></div>
  </div>
</section>

<section class="cash abs">
  <svg class="abs" style="left:0;top:0" width="667" height="229" viewBox="0 0 667 229">
    <rect width="667" height="229" fill="#2b9be3"/>
    <polygon points="330,0 667,0 667,229 250,229" fill="#0d3f86"/>
    <polygon points="318,0 330,0 250,229 238,229" fill="#ffffff"/>
  </svg>
  <div class="cash-title abs">GET CASH<br><span>FOR YOUR</span><br>HOUSE!</div>
  <p class="cash-copy abs">We buy houses for cash in any shape, any area and any price range. Skip the listing, the open houses and the long wait for a buyer.</p>
  <div class="photo abs" style="left:150px;top:40px;width:150px;height:150px;background:radial-gradient(circle at 40% 40%,#d9d6cf,#8b8577)" role="img" aria-label="Photo of a weathered house in need of repairs"></div>
  <div class="photo abs" style="left:342px;top:60px;width:98px;height:98px;background:radial-gradient(circle at 50% 40%,#c6d3dc,#6d7d6b)" role="img" aria-label="Photo of a for sale sign in front of a house"></div>
  <ul class="benefits abs">
    <li>We Pay All Cash</li>
    <li>We Pay Most Closing Costs</li>
    <li>We buy "as is"</li>
    <li>No Waiting For Bank Loan Approvals</li>
    <li>Quick Closings</li>
  </ul>
  <div class="fastest abs"><b>FASTEST<br>WAY!</b><span>TO SELL YOUR HOME</span></div>
</section>

<div class="more-info abs">GET MORE INFO ›</div>

<section class="condition abs">
  <div class="photo abs" style="left:70px;top:20px;width:150px;height:150px;border-color:var(--blue);background:radial-gradient(circle at 50% 45%,#c8d2d8,#77806f)" role="img" aria-label="Photo of a family home with a green lawn"></div>
  <h2 class="abs">WE BUY HOUSES IN <em>ANY CONDITION!</em></h2>
  <p class="abs">Don't waste another penny on expensive repairs! DORLIT HOMES is currently buying houses throughout the area. We buy houses "as is", we pay cash, we handle all closing costs and we can close in as quickly as a week. Contact us today for your free, no-obligation quote.</p>
  <span class="btn-quote abs">GET YOUR FREE QUOTE ›</span>
</section>

<footer class="site-footer abs">
  <div class="fcol abs" style="left:22px">
    <h4>QUICK LINKS</h4>
    <ul><li>HOME</li><li>ABOUT US</li><li>FAQ</li><li>CONTACT US</li><li>TESTIMONIALS</li><li>HOUSES TO BUY</li></ul>
  </div>
  <div class="fcol abs" style="left:170px">
    <h4>CONTACT DETAILS</h4>
    <div class="contact-row"><span class="dot"></span><span>DORLIT HOMES<br>Local office, open<br>weekdays nine to five</span></div>
    <div class="contact-row"><span class="dot"></span><span>418-555-0193</span></div>
    <div class="contact-row"><span class="dot"></span><span>info@dorlithomes.com</span></div>
  </div>
  <div class="fcol abs" style="left:330px">
    <h4>SOCIAL MEDIA</h4>
    <div class="social-row"><span class="dot"></span>COMMUNITY</div>
    <div class="social-row"><span class="dot"></span>UPDATES</div>
    <div class="social-row"><span class="dot"></span>REVIEWS</div>
    <div class="social-row"><span class="dot"></span>NETWORK</div>
  </div>
  <div class="footer-brand abs">DORLIT HOMES</div>
  <div class="copyright abs">Copyright 2015 DORLIT HOMES<br>All Rights Reserved.</div>
</footer>

</body>
</html>
```